Business Card Design Project

Business Card
We are rebranding with a new logo
Industry/Entity Type
Business
Contact Information for Business Card
Dennis Marlow +61 427581962 dennis@qovo.com.au P.O. Box 872 Kelvindale QLD 4309
Requirements
Must have
- Logo

```html
<!DOCTYPE html>
<html lang="en">
<head>
<meta charset="utf-8">
<title>Dennis Marlow – Business Card</title>
<link rel="stylesheet" href="https://fonts.googleapis.com/css2?family=Arvo:wght@400;700&family=Raleway:wght@300&display=swap">
<style>
  :root {
    --ink: #1b1b1b;
    --paper: #ffffff;
    --accent: #00ffff;
    --icon: #1fe3ea;
    --text-light: #ffffff;
    --brand: #1f6fb8;
  }
  * { margin: 0; padding: 0; box-sizing: border-box; }
  html, body {
    width: 1200px; height: 720px; overflow: hidden;
    background: var(--paper);
  }
  .card {
    position: relative; width: 1200px; height: 720px;
    background: var(--paper); overflow: hidden;
    font-family: "Arvo", Georgia, serif;
    color: var(--text-light);
  }
  .card__shapes { position: absolute; inset: 0; }
  .card__shapes .panel { fill: var(--ink); }
  .card__shapes .wedge { fill: var(--accent); }

  .contact-row {
    position: absolute; left: 99px;
    display: flex; align-items: center; gap: 30px;
  }
  .icon-box {
    width: 49px; height: 49px; flex: none;
    border: 2px solid var(--text-light);
    display: flex; align-items: center; justify-content: center;
  }
  .icon-box svg { width: 30px; height: 30px; }
  .icon-box .stroke { fill: none; stroke: var(--icon); stroke-width: 1.6; stroke-linecap: round; stroke-linejoin: round; }
  .icon-box .fill { fill: var(--icon); }

  .row-name { top: 196px; align-items: flex-start; }
  .row-name .icon-box { margin-top: 13px; }
  .person__name { font-weight: 700; font-size: 42px; line-height: 1.05; letter-spacing: 0.5px; }
  .person__role {
    font-family: "Raleway", Arial, sans-serif; font-weight: 300;
    font-size: 29px; line-height: 1.1; letter-spacing: 0.5px;
  }

  .row-phone { top: 313px; }
  .row-phone .contact-text { font-size: 28px; }

  .row-web { top: 408px; }
  .row-address { top: 502px; }
  .contact-text { font-size: 23.5px; line-height: 32px; }

  .brand {
    position: absolute; left: 712px; top: 286px; width: 400px;
    text-align: center; color: var(--brand);
    font-family: "Arvo", Georgia, serif; font-weight: 700;
    font-size: 46px; line-height: 1.2;
  }
</style>
</head>
<body>
<main class="card">
  <svg class="card__shapes" viewBox="0 0 1200 720" width="1200" height="720" aria-hidden="true">
    <polygon class="wedge" points="600,0 780,0 690,178"/>
    <polygon class="wedge" points="690,537 780,720 600,720"/>
    <polygon class="panel" points="0,0 600,0 690,178 600,360 690,537 600,720 0,720"/>
  </svg>

  <div class="contact-row row-name">
    <div class="icon-box">
      <svg viewBox="0 0 30 30"><circle class="stroke" cx="15" cy="10" r="5"/><path class="stroke" d="M5 26v-3c0-4 4-7 10-7s10 3 10 7v3z"/></svg>
    </div>
    <div>
      <div class="person__name">Dennis Marlow</div>
      <div class="person__role">DESIGNATION</div>
    </div>
  </div>

  <div class="contact-row row-phone">
    <div class="icon-box">
      <svg viewBox="0 0 30 30"><path class="fill" d="M4 11c0-3 5-5 11-5s11 2 11 5v2h-5v-3h-12v3h-5z"/><path class="fill" d="M8 13h14l3 11h-20z"/><circle cx="15" cy="19" r="3.2" fill="#1b1b1b"/></svg>
    </div>
    <div class="contact-text">+61 427581962</div>
  </div>

  <div class="contact-row row-web">
    <div class="icon-box">
      <svg viewBox="0 0 30 30"><circle class="stroke" cx="15" cy="15" r="11"/><ellipse class="stroke" cx="15" cy="15" rx="5" ry="11"/><path class="stroke" d="M4 15h22M6 9h18M6 21h18M15 4v22"/></svg>
    </div>
    <div class="contact-text">dennis@qovo.com.au<br>www.websiteurl.com</div>
  </div>

  <div class="contact-row row-address">
    <div class="icon-box">
      <svg viewBox="0 0 30 30"><path class="fill" d="M15 3c-5 0-8.5 3.6-8.5 8.3 0 5.7 8.5 15.7 8.5 15.7s8.5-10 8.5-15.7C23.5 6.6 20 3 15 3z"/><circle cx="15" cy="11" r="3.2" fill="#1b1b1b"/></svg>
    </div>
    <div class="contact-text">P.O. Box 872 Kelvindale<br>QLD 4309</div>
  </div>

  <div class="brand">Qovo<br>International</div>
</main>
</body>
</html>
```